Redesign Current Website Into An Exciting Updated Design

We need to redesign the current website www.glintvaultoffers.net We want an overall new look. We are rebranding so it will be a new logo and we would like to see new images as well so you cannot compare the old from the new.

You can use same exact content as on current url www.glintvaultoffers.net

The website must be warm and inviting and fun yet professional and modern.

The website must also be designed with mobile in mind

The website must be warm and inviting yet professional and modern.

The website must also be designed with mobile in mind.

Target Market(s)

Consumers redeeming rewards

Industry/Entity Type

Promotional Reward Fullfillment

Coding

Coded - Design and coding required

Number of Pages Required

3 page

Requirements
Must have
• This website is a website where consumers come to redeem rewards they received from doing business with a company that offers these rewards. So the website should be very inviting.
Nice to have
• open
Should not have
• open

```html
<!DOCTYPE html>
<html lang="en">
<head>
<meta charset="utf-8">
<title>Glint Vault Offers – Online Redemption System</title>
<link rel="stylesheet" href="https://fonts.googleapis.com/css2?family=Oswald:wght@500;600&family=Poppins:ital,wght@0,400;0,500;1,400&display=swap">
<style>
:root{
  --blue:#2b6699;
  --blue-deep:#245c8c;
  --blue-mid:#3a78ad;
  --sky:#e8f2fc;
  --sky-2:#d3e6f8;
  --ink:#333b44;
  --muted:#8a96a3;
  --line:#7fa9cf;
  --white:#ffffff;
}
*{box-sizing:border-box;margin:0;padding:0}
html,body{width:1200px;height:4542px;overflow:hidden;background:var(--white)}
body{font-family:'Poppins',sans-serif;color:var(--ink);position:relative}
.abs{position:absolute}
.head{font-family:'Oswald',sans-serif;font-weight:600;color:var(--blue);text-transform:uppercase;letter-spacing:.5px}

/* brand */
.brand{font-family:'Oswald',sans-serif;font-weight:600;color:var(--blue);font-size:38px;line-height:38px;text-transform:uppercase}
.brand--light{color:var(--white)}

/* nav */
.nav{top:54px;left:578px;display:flex;gap:0}
.nav a{font-family:'Oswald',sans-serif;font-weight:500;font-size:15px;color:var(--blue);text-decoration:none;text-transform:uppercase;position:absolute;white-space:nowrap}

/* hero */
.hero-title{left:127px;top:250px;font-size:44px;line-height:44px}
.hero-text{left:127px;top:354px;width:440px;font-size:16px;line-height:26px}
.field{height:48px;border:1.5px solid #9aa3ad;border-radius:24px;font-size:15px;padding:0 18px;display:flex;align-items:center;color:#555;background:var(--white)}
.btn{display:flex;align-items:center;justify-content:center;font-family:'Oswald',sans-serif;font-weight:500;text-transform:uppercase;font-size:15px;border-radius:30px;text-decoration:none}
.btn--solid{background:var(--blue);color:var(--white)}
.btn--ghost{border:2px solid var(--white);color:var(--white)}
.placeholder{border-radius:4px}

/* section heading frame */
.frame-title{position:absolute;padding:14px 18px 4px 20px}
.frame-title::before{content:"";position:absolute;left:0;top:0;width:2px;height:100%;background:currentColor}
.frame-title::after{content:"";position:absolute;left:0;top:0;width:40px;height:2px;background:currentColor}
.frame-title .underline{position:absolute;left:0;right:0;bottom:-4px;height:2px;background:currentColor}

/* offers */
.offers{background:var(--blue)}
.offer{position:absolute;left:663px;width:354px;height:62px;border-bottom:1.5px solid var(--line);display:flex;align-items:center}
.offer svg{width:44px;height:34px;margin-left:4px}
.offer span{margin-left:26px;font-family:'Oswald',sans-serif;font-weight:500;font-size:22px;color:var(--white);text-transform:uppercase}

/* testimonial */
.card{left:127px;top:1730px;width:944px;height:379px;border:3px solid var(--blue);background:var(--white)}
.quote{left:176px;top:1796px;width:380px;font-style:italic;font-size:20px;line-height:28px;color:#222}
.dots{top:2174px;left:568px;display:flex;gap:5px}
.dots i{width:8px;height:8px;border-radius:50%;background:#c9d7e5;display:block}
.dots i:first-child{background:var(--blue)}

/* about */
.copy{font-size:14.6px;line-height:20.8px;color:#2d333a}
.copy p+p{margin-top:20px}

/* clients */
.client{position:absolute;width:180px;height:94px;border:1.5px solid #a9bdd2;display:flex;align-items:center;justify-content:center;font-family:'Poppins',sans-serif;font-weight:500;font-size:17px;color:var(--muted);background:var(--white);text-align:center}

/* footer */
.foot-links{left:400px;top:4386px;width:400px;text-align:center;color:var(--white);font-size:16px;line-height:32px}
</style>
</head>
<body>

<!-- hero backdrop -->
<svg class="abs" style="left:0;top:0" width="1200" height="714" viewBox="0 0 1200 714" aria-hidden="true">
  <path d="M980 0 C930 60 920 120 950 170 C990 240 900 300 790 380 C690 450 690 560 760 630 C820 690 1050 700 1200 690 L1200 0 Z" fill="var(--sky-2)"/>
</svg>

<header>
  <div class="abs brand" style="left:127px;top:64px">Glint Vault<br>Offers</div>
  <nav class="abs nav">
    <a href="#testimonials" style="left:0">Testimonials</a>
    <a href="#redeemed" style="left:143px">Already Redeemed?</a>
    <a href="#help" style="left:333px">Help</a>
  </nav>
</header>

<section class="hero">
  <h1 class="abs head hero-title">Welcome to the online<br>redemption system</h1>
  <p class="abs hero-text">To Learn More About Your Offer Including The Full Details, How It Works, Terms, FAQ's and To Redeem and Activate Your Certificate Please Enter A Valid Certificate Number and Email.</p>
  <div class="abs field" style="left:127px;top:497px;width:423px">Certificate ID</div>
  <div class="abs field" style="left:127px;top:559px;width:276px">Enter Email Address</div>
  <a class="abs btn btn--solid" style="left:409px;top:559px;width:142px;height:49px" href="#start">Start Now</a>
  <div class="abs placeholder" role="img" aria-label="Illustration of a woman choosing a gift box on a large smartphone screen with shopping icons, coins and leaves" style="left:696px;top:180px;width:470px;height:440px;background:linear-gradient(160deg,#cfe2f6,#4a86c2);border-radius:20px"></div>
</section>

<section class="offers abs" style="left:0;top:714px;width:1200px;height:745px">
  <div class="abs" role="img" aria-label="Illustration of a hand offering a wrapped gift box to a businessman in a blue suit" style="left:0;top:132px;width:580px;height:476px;background:linear-gradient(90deg,#3573a8,#2f6da2);border-radius:4px"></div>
  <h2 class="frame-title head" style="left:650px;top:88px;color:var(--white);font-size:40px;line-height:44px"><span style="color:var(--white)">Redeem your offers</span><span class="underline"></span></h2>

  <div class="offer" style="top:198px">
    <svg viewBox="0 0 44 34" fill="none" stroke="#fff" stroke-width="1.8"><rect x="3" y="5" width="38" height="24" rx="2"/><rect x="8" y="10" width="28" height="14"/><line x1="13" y1="17" x2="31" y2="17"/></svg>
    <span>Vacation certificates</span></div>
  <div class="offer" style="top:266px">
    <svg viewBox="0 0 44 34" fill="none" stroke="#fff" stroke-width="1.8"><rect x="3" y="6" width="38" height="22" rx="2"/><circle cx="14" cy="17" r="5"/><line x1="24" y1="13" x2="36" y2="13"/><line x1="24" y1="20" x2="33" y2="20"/></svg>
    <span>Travel vouchers</span></div>
  <div class="offer" style="top:335px">
    <svg viewBox="0 0 44 34" fill="none" stroke="#fff" stroke-width="1.8"><rect x="14" y="8" width="16" height="18" rx="4"/><line x1="17" y1="2" x2="27" y2="2"/><line x1="17" y1="32" x2="27" y2="32"/></svg>
    <span>Digital electronic products</span></div>
  <div class="offer" style="top:404px">
    <svg viewBox="0 0 44 34" fill="none" stroke="#fff" stroke-width="1.8"><path d="M12 28 L12 14 L18 6 L20 14 L30 14 L28 28 Z"/><line x1="6" y1="14" x2="6" y2="28"/></svg>
    <span>Dining incentives</span></div>
  <div class="offer" style="top:473px">
    <svg viewBox="0 0 44 34" fill="none" stroke="#fff" stroke-width="1.8"><path d="M6 12 L10 4 L34 4 L38 12 Z"/><rect x="8" y="12" width="28" height="18"/><rect x="12" y="17" width="8" height="13"/><rect x="24" y="17" width="8" height="7"/></svg>
    <span>Gas grocery rewards</span></div>

  <a class="abs btn btn--ghost" style="left:663px;top:586px;width:257px;height:60px" href="#redeem">Redeem your offer now</a>
</section>

<!-- light area with waves -->
<svg class="abs" style="left:0;top:2030px" width="1200" height="1580" viewBox="0 0 1200 1580" aria-hidden="true">
  <path d="M0 230 C200 150 340 160 520 190 C760 230 960 200 1080 110 C1140 60 1180 20 1200 0 L1200 1580 L0 1580 Z" fill="var(--sky)"/>
</svg>
<svg class="abs" style="left:1030px;top:1780px" width="170" height="300" viewBox="0 0 170 300" aria-hidden="true">
  <path d="M170 0 C120 60 70 120 80 200 C90 250 130 280 170 300 Z" fill="var(--sky)"/>
</svg>

<section id="testimonials">
  <h2 class="frame-title head" style="left:476px;top:1614px;color:var(--blue);font-size:40px;line-height:44px">Testimonials<span class="underline"></span></h2>
  <div class="abs card"></div>
  <div class="abs" role="img" aria-label="Photo of a traveller in a sun hat sitting in a wooden boat on turquoise water between cliffs" style="left:611px;top:1733px;width:457px;height:373px;background:linear-gradient(180deg,#6d7d68,#2e8c92 55%,#8a6a4a)"></div>
  <blockquote class="abs quote">“Wonderful! It was just like being in Rome, but only with great shows to enjoy. The rooms of the Marivento and service were excellent. Going through the travel agency was simple and easy on the purse strings.”</blockquote>
  <p class="abs head" style="left:176px;top:1998px;font-size:28px">Martin K.</p>
  <p class="abs" style="left:176px;top:2040px;font-size:15px;color:#555">Cedar Ridge, AZ</p>
  <div class="abs dots"><i></i><i></i><i></i><i></i><i></i></div>
</section>

<section class="about">
  <h2 class="frame-title head" style="left:508px;top:2341px;color:var(--blue);font-size:40px;line-height:44px">About us<span class="underline"></span></h2>
  <div class="abs copy" style="left:127px;top:2484px;width:505px">
    <p>We provide marketing incentives in the form of gift certificates and vouchers that are redeemable for a variety of items such as: discount travel, smart device products, restaurant incentives , golf discounts and more to thousands of businesses around the world who use them to create exciting marketing promotions and giveaways, customer loyalty programs, promotional contests and use them as customer appreciation gifts.</p>
    <p>We are simply a 3rd party administrator that handles the redemption and fulfillment processing for a variety of incentive gifts and rewards. We have created the platform that facilitates the redemption and fulfillment process in a comprehensive, an easy to use online interface. Simply enter your code and email to redeem your offer and follow the steps to complete the fulfillment process to receive your gift. We work with thousands of large corporations and even small independently owned businesses that trust us to take care of their customers. It's our goal to make it easy for you to redeem your offer.</p>
  </div>
  <div class="abs" role="img" aria-label="Photo of a smiling woman in glasses looking at her phone as banknotes fly around her" style="left:678px;top:2479px;width:394px;height:406px;background:linear-gradient(150deg,#9a9a94,#c9a46e 55%,#5e6a60)"></div>
  <div class="abs" role="img" aria-label="Photo of hands holding a smartphone with glowing dollar signs rising above it" style="left:127px;top:2886px;width:368px;height:507px;background:linear-gradient(180deg,#5d7a62,#3f5745 60%,#8a8a7a)"></div>
  <div class="abs copy" style="left:532px;top:2942px;width:540px">
    <p>We never market or distribute our incentives to end users as our business model is selling them to businesses and they distribute them to their customers through creative marketing strategies. The only way the recipient can get their hands on one of the certificates and vouchers is by participating in a promotion from one of the thousands of businesses around the world that currently use our marketing incentives in their advertising efforts.</p>
    <p>Since we do not ever distribute certificates to end users and only facilitate the redemption and fulfillment process, we can only honor what is stated in the terms and conditions of the offer. Be sure to read all the details, terms and frequently asked questions regarding your offer to better understand how your offer works. Our vendors, whom we contract with to make these offers happen are responsible for providing the specific terms and conditions in order to use the offer and we simply play as a middle man and a 3rd party administrator to facilitate the fulfillment process while enforcing the requirements. If you ever need to get a hold of us, simply login to the website by entering your certificate number and email at the top of this page and then by clicking on the red Support tab located in the lower right hand corner of your dashboard. We look forward to facilitating the process from start to finish.</p>
  </div>
  <a class="abs btn btn--solid" style="left:472px;top:3445px;width:255px;height:61px" href="#redeem">Redeem your offer now</a>
</section>

<section class="clients">
  <h2 class="frame-title head" style="left:476px;top:3672px;color:var(--blue);font-size:40px;line-height:44px">Our clients<span class="underline"></span></h2>
  <p class="abs" style="left:0;top:3790px;width:1200px;text-align:center;font-size:16px;color:#555">A few of our clients that we redeem and fulfill gift certificates and rewards for</p>
  <div class="client" style="left:127px;top:3836px">Harbor Mutual</div>
  <div class="client" style="left:318px;top:3836px">Fieldstone Cover</div>
  <div class="client" style="left:509px;top:3836px">Wellpath Plans</div>
  <div class="client" style="left:700px;top:3836px">Keystone Realty</div>
  <div class="client" style="left:891px;top:3836px">Oakmere Homes</div>
  <div class="client" style="left:222px;top:3944px">Homeline Direct</div>
  <div class="client" style="left:413px;top:3944px">Torvik Motors</div>
  <div class="client" style="left:604px;top:3944px">Skyreach TV</div>
  <div class="client" style="left:795px;top:3944px">Northgate Realty</div>
  <a class="abs btn btn--solid" style="left:472px;top:4077px;width:255px;height:61px" href="#redeem">Redeem your offer now</a>
</section>

<footer>
  <svg class="abs" style="left:0;top:4170px" width="1200" height="372" viewBox="0 0 1200 372" aria-hidden="true">
    <path d="M0 40 C220 0 420 60 640 40 C860 20 1020 -10 1200 30 L1200 372 L0 372 Z" fill="var(--sky-2)"/>
    <path d="M0 60 C200 110 420 30 640 70 C860 110 1040 50 1200 80 L1200 372 L0 372 Z" fill="var(--blue)"/>
  </svg>
  <div class="abs brand brand--light" style="left:127px;top:4350px">Glint Vault<br>Offers</div>
  <div class="abs foot-links"><p>Privacy Policy - Terms Of Use</p><p>© Copyright 2025. All Rights Reserved.</p></div>
  <a class="abs btn btn--ghost" style="left:814px;top:4382px;width:258px;height:62px" href="#redeem">Redeem your offer now</a>
</footer>

</body>
</html>
```